Book Cover Design Project For New Nonfiction book

I need a cover designed for a new book/eBook - Little Savers Handbook for Trimming Your Household’s Waste Trail by Moira Fenwick.
Below is a description of the book. I don't have a specific idea or vision in mind for the cover. I'd like to see what designs and ideas ArtHuddle designers come up with.
However, the design needs to work and be effective at both a large book cover size and a small thumbnail-sized image - the way that many people browse book covers on Bookvane and other websites. Therefore, a design that relies on really small details probably won't translate at the smaller image sizes that book covers are displayed online. Just keep that in mind!
Little Savers Handbook for Trimming Your Household’s Waste Trail by Moira Fenwick will help you and your family make your way of life greener: by wasting less, reusing and recycling more. Step-by-step, Moira Fenwick will show you how you can:
• LIVE a much greener lifestyle without sacrificing much in the way of convenience or time
• HARNESS your children’s natural concern about people and the planet
• EMPOWER your children by helping them improve the world
• SAVE your family gobs of money!
• TRACK your progress with a table at the back of the book, to see how much electricity, water, heat, and cash you save!
Following even just a few of the 102 tips in this ebook can have a big impact on your family's economic savings - and the planet!
Target Market(s)
The book is designed to be read by parents and child
Industry/Entity Type
Recycling
Look and feel

```html
<!DOCTYPE html>
<html lang="en">
<head>
<meta charset="utf-8">
<title>Little Savers Handbook – Cover Presentation</title>
<link href="https://fonts.googleapis.com/css2?family=Cinzel:wght@400;500&family=Oswald:wght@500&family=Roboto+Condensed:wght@700&display=swap" rel="stylesheet">
<style>
  :root {
    --page-bg: #ffffff;
    --sky-top: #2a78d2;
    --sky-mid: #86c3ef;
    --haze: #f3f5dc;
    --meadow: #cfe49a;
    --grass: #5f9b22;
    --leaf: #4f9a2a;
    --band-top: #2f6a12;
    --band-bottom: #173f08;
    --title-white: #ffffff;
    --tips-orange: #f26a1b;
    --tips-blue: #1f6fc2;
    --tips-green: #58a723;
    --text-shadow: rgba(10, 30, 60, 0.75);
  }
  * { margin: 0; padding: 0; box-sizing: border-box; }
  html, body {
    width: 1200px; height: 960px; overflow: hidden;
    background: var(--page-bg);
  }
  .stage { position: relative; width: 1200px; height: 960px; }

  .cover-slot { position: absolute; }
  .cover-slot--large { left: 444px; top: 22px; width: 726px; height: 918px; }
  .cover-slot--medium { left: 82px; top: 434px; width: 221px; height: 279px; }
  .cover-slot--small { left: 130px; top: 234px; width: 128px; height: 162px; }

  .cover {
    position: absolute; left: 0; top: 0;
    width: 726px; height: 918px; overflow: hidden;
    transform-origin: 0 0;
    box-shadow: 6px 8px 14px rgba(0, 0, 0, 0.35);
  }
  .cover-slot--medium .cover { transform: scale(0.3044); box-shadow: 14px 18px 30px rgba(0,0,0,0.35); }
  .cover-slot--small .cover { transform: scale(0.1763); box-shadow: 22px 28px 40px rgba(0,0,0,0.35); }

  .cover__art {
    position: absolute; left: 0; top: 0; width: 726px; height: 818px;
    background:
      radial-gradient(ellipse 300px 320px at 590px 470px, var(--leaf) 0%, rgba(79,154,42,0.85) 55%, rgba(79,154,42,0) 100%),
      radial-gradient(circle 60px at 560px 110px, rgba(255,255,255,0.9), rgba(255,255,255,0) 100%),
      linear-gradient(to bottom, rgba(95,155,34,0) 0%, rgba(95,155,34,0) 88%, var(--grass) 100%),
      linear-gradient(to bottom, var(--sky-top) 0%, var(--sky-mid) 42%, var(--haze) 74%, var(--meadow) 86%);
  }

  .cover__title {
    position: absolute; left: 40px; top: 18px;
    font-family: "Cinzel", serif; font-weight: 400;
    color: var(--title-white);
    text-shadow: 2px 3px 4px var(--text-shadow);
    line-height: 1;
  }
  .cover__title-line { display: block; }
  .cover__title-line--first { font-size: 118px; letter-spacing: -2px; }
  .cover__title-line--second { font-size: 86px; margin-top: 18px; margin-left: 44px; letter-spacing: 1px; }

  .cover__subtitle {
    position: absolute; left: 42px; top: 300px;
    font-family: "Oswald", sans-serif; font-weight: 500;
    font-size: 42px; line-height: 54px;
    color: var(--title-white);
    text-shadow: 2px 2px 3px var(--text-shadow);
  }

  .cover__tips {
    position: absolute; left: 42px; top: 612px;
    font-family: "Roboto Condensed", sans-serif; font-weight: 700;
    text-shadow: 1px 2px 2px rgba(255,255,255,0.8);
  }
  .cover__tips-count { display: block; font-size: 64px; line-height: 70px; color: var(--tips-orange); }
  .cover__tips-line { display: block; font-size: 28px; line-height: 38px; color: var(--tips-blue); }
  .cover__tips-line--one { margin-left: 24px; }
  .cover__tips-line--two { margin-left: 48px; }
  .cover__tips-accent { color: var(--tips-green); }

  .cover__band {
    position: absolute; left: 0; top: 818px; width: 726px; height: 100px;
    background: linear-gradient(to bottom, var(--band-top), var(--band-bottom));
    display: flex; align-items: center; justify-content: center;
  }
  .cover__author {
    font-family: "Cinzel", serif; font-weight: 500;
    font-size: 36px; letter-spacing: 1px;
    color: var(--title-white);
    text-shadow: 1px 2px 3px rgba(0,0,0,0.6);
  }
</style>
</head>
<body>
<main class="stage">

  <div class="cover-slot cover-slot--small">
    <article class="cover">
      <div class="cover__art" role="img" aria-label="Illustration of a bright blue sky with clouds and sun, a large leafy green tree on the right and a grassy meadow"></div>
      <h1 class="cover__title"><span class="cover__title-line cover__title-line--first">LITTLE</span><span class="cover__title-line cover__title-line--second">SAVERS</span></h1>
      <p class="cover__subtitle">Handbook for Trimming<br>Your Household’s<br>Waste Trail</p>
      <p class="cover__tips"><span class="cover__tips-count">88 Ideas</span><span class="cover__tips-line cover__tips-line--one">for a <span class="cover__tips-accent">Cleaner</span> Home</span><span class="cover__tips-line cover__tips-line--two">and Family Budget.</span></p>
      <div class="cover__band"><p class="cover__author">BY MOIRA FENWICK</p></div>
    </article>
  </div>

  <div class="cover-slot cover-slot--medium">
    <article class="cover">
      <div class="cover__art" role="img" aria-label="Illustration of a bright blue sky with clouds and sun, a large leafy green tree on the right and a grassy meadow"></div>
      <h1 class="cover__title"><span class="cover__title-line cover__title-line--first">LITTLE</span><span class="cover__title-line cover__title-line--second">SAVERS</span></h1>
      <p class="cover__subtitle">Handbook for Trimming<br>Your Household’s<br>Waste Trail</p>
      <p class="cover__tips"><span class="cover__tips-count">88 Ideas</span><span class="cover__tips-line cover__tips-line--one">for a <span class="cover__tips-accent">Cleaner</span> Home</span><span class="cover__tips-line cover__tips-line--two">and Family Budget.</span></p>
      <div class="cover__band"><p class="cover__author">BY MOIRA FENWICK</p></div>
    </article>
  </div>

  <div class="cover-slot cover-slot--large">
    <article class="cover">
      <div class="cover__art" role="img" aria-label="Illustration of a bright blue sky with clouds and sun, a large leafy green tree on the right and a grassy meadow"></div>
      <h1 class="cover__title"><span class="cover__title-line cover__title-line--first">LITTLE</span><span class="cover__title-line cover__title-line--second">SAVERS</span></h1>
      <p class="cover__subtitle">Handbook for Trimming<br>Your Household’s<br>Waste Trail</p>
      <p class="cover__tips"><span class="cover__tips-count">88 Ideas</span><span class="cover__tips-line cover__tips-line--one">for a <span class="cover__tips-accent">Cleaner</span> Home</span><span class="cover__tips-line cover__tips-line--two">and Family Budget.</span></p>
      <div class="cover__band"><p class="cover__author">BY MOIRA FENWICK</p></div>
    </article>
  </div>

</main>
</body>
</html>
```